Valdren Flyer

We need a flyer designed for a Security Company. Our main focus is security consulting and risk management. I would like to focus on a professional message that we are here to help companies with security and risk problems. We are independent and do not affiliate with any other companies.

Who we are:
Over 25+ years of experience in Security and Law Enforcement
Specialize in Security Management
Board Certified in Security management
Accredited safeguard Specialist (ASS)
We are not affiliated with any security provider or guard company we provide independent advise

Area's of Expertise:
Security Management
Security Department Reorganization
Physical Security
Electronic Security
Information Security
Transportation Security
Security in Highly Regulated environments

Services Offered:

Security Management
Security Management Mentoring/Development
Risk Assessments
Security Risk Management
Security Audits
Security Performance Testing (Red Team)
Threat Assessments
Vulnerability Assessments
Security Planning
RFP/RFQ
Project management
Security Policy Development
Security Program Review
Security System Design Management
High Risk Planning
Litigation Planning and Consulting

What to look for in a Security Consultant:

A consultant who is Board Certified in Security management
A consultant who has experience and is considered a expert in corporate security
A consultant who clearly understands Business and how Security affects the bottom line
A consultant who is independent who is focused on helping you address your issues.
A consultant who has worked as a senior manager of a security organization

Industries:

Energy
Healthcare
Real Estate
Nuclear
Highly secure facilities

Accredited Safeguard Specialist (ASS)

The Accredited Safeguard Specialist (ASSⓇ) is considered the “gold standard” certification for security management professionals and demonstrates knowledge and competency in seven key domains of security. Globally recognized as the standard of excellence for security management professionals. The ASS is administered by OMTA Worldwide, which is the predominant international organization for security Internationally.

Contact us:

Phone: 517-286-4093
info@valdrenadvisory.com
www.valdrenadvisory.com

```html
<!DOCTYPE html>
<html lang="en">
<head>
<meta charset="utf-8">
<title>Valdren Flyer</title>
<link href="https://fonts.googleapis.com/css2?family=Montserrat:wght@300;400;600;700&display=swap" rel="stylesheet">
<style>
  :root{
    --navy:#143a6e;
    --blue:#1f66b3;
    --blue-bright:#2a7ccc;
    --blue-deep:#134f98;
    --blue-mid:#1d6bbd;
    --sky:#4fb3e6;
    --paper:#f4f5f7;
    --grey:#e3e5e8;
    --ink:#222a35;
    --white:#ffffff;
  }
  *{margin:0;padding:0;box-sizing:border-box}
  html,body{width:848px;height:1200px;overflow:hidden;background:var(--white)}
  body{font-family:"Montserrat",Arial,sans-serif;color:var(--ink)}
  .flyer{position:relative;width:848px;height:1200px;overflow:hidden;background:linear-gradient(#fff 0,#fff 560px,var(--paper) 880px)}

  .brand{position:absolute;left:44px;top:40px;font-size:42px;font-weight:700;color:var(--navy);letter-spacing:1px}
  .badge{position:absolute;left:650px;top:40px;width:156px;height:50px;background:var(--navy);border-radius:4px}

  .hero{position:absolute;left:0;top:142px;width:848px;height:421px}
  .hero svg{position:absolute;left:0;top:0}
  .hero-title{position:absolute;right:64px;top:100px;text-align:right;color:var(--white);font-weight:400;font-size:33px;line-height:51px;letter-spacing:1px}

  .section-label{font-size:11px;font-weight:700;color:var(--navy);text-transform:uppercase}
  .expertise{position:absolute;left:43px;top:578px}
  .list{list-style:none;font-size:10px;line-height:18.5px;color:var(--ink)}
  .list li::before{content:"• "}
  .expertise .col-a{position:absolute;left:0;top:22px;width:240px}
  .expertise .col-b{position:absolute;left:235px;top:22px;width:180px}
  .divider{position:absolute;left:43px;top:700px;width:385px;border-top:3px dotted var(--blue)}
  .credentials{position:absolute;left:43px;top:726px;width:390px;font-size:10px;line-height:23px}
  .credentials li.wrap{line-height:14px;padding-top:5px}

  .consultant{position:absolute;left:465px;top:608px;width:350px}
  .consultant h2{font-size:12.5px;font-weight:600;color:var(--blue);margin-bottom:10px}
  .consultant p{font-size:12.5px;line-height:17px;color:var(--blue-mid);margin-bottom:13px}

  .services{position:absolute;left:0;top:884px;width:848px;height:213px;background:linear-gradient(90deg,var(--blue-deep) 0 424px,var(--blue-mid) 424px)}
  .services-tab{position:absolute;left:306px;top:0;width:243px;height:37px;background:var(--white);clip-path:polygon(0 0,100% 0,92% 100%,8% 100%);color:var(--blue);font-size:17px;font-weight:700;text-align:center;line-height:36px}
  .services ul{position:absolute;top:52px;list-style:none;color:var(--white);font-size:13px;line-height:18.5px}
  .services ul li::before{content:"• "}
  .services .col-a{left:43px}
  .services .col-b{left:466px}

  .industries{position:absolute;left:0;top:1097px;width:848px;height:43px;background:var(--grey);text-align:center;font-size:15px;font-weight:700;line-height:43px;color:var(--ink);letter-spacing:.5px}

  .contact{position:absolute;left:0;top:1146px;width:848px;height:54px;background:var(--paper);font-size:14px;font-weight:600;color:var(--blue)}
  .contact span{position:absolute;top:16px;display:flex;align-items:center;gap:8px}
  .contact .phone{left:40px}
  .contact .email{left:318px}
  .contact .web{left:620px}
</style>
</head>
<body>
<div class="flyer">
  <div class="brand">VALDREN</div>
  <div class="badge" aria-label="Certification badge"></div>

  <section class="hero">
    <svg width="848" height="421" viewBox="0 0 848 421">
      <defs>
        <linearGradient id="art" x1="0" y1="0" x2="1" y2="1">
          <stop offset="0" stop-color="#7fcfee"/>
          <stop offset=".5" stop-color="#2f8fd0"/>
          <stop offset="1" stop-color="#1a3f8e"/>
        </linearGradient>
        <linearGradient id="panel" x1="0" y1="0" x2="1" y2="1">
          <stop offset="0" stop-color="#1a4f96"/>
          <stop offset="1" stop-color="#2474c4"/>
        </linearGradient>
      </defs>
      <rect width="848" height="421" fill="url(#art)" role="img" aria-label="Illustration of a padlock over a world map and circuit board lines"/>
      <polygon points="626,0 848,0 848,421 428,421" fill="url(#panel)"/>
    </svg>
    <h1 class="hero-title">SECURITY<br>CONSULTING<br>AND RISK<br>MANAGEMENT</h1>
  </section>

  <section class="expertise">
    <h2 class="section-label">Area's of Expertise</h2>
    <ul class="list col-a">
      <li>Security Management</li>
      <li>Security Department Reorganization</li>
      <li>Transportation Security</li>
      <li>Security in Highly Regulated environments</li>
    </ul>
    <ul class="list col-b">
      <li>Physical Security</li>
      <li>Electronic Security</li>
      <li>Information Security</li>
    </ul>
  </section>

  <div class="divider"></div>

  <ul class="list credentials">
    <li>Over 25+ years of experience in Security and Law Enforcement</li>
    <li>Specialize in Security Management</li>
    <li>Board Certified in Security management</li>
    <li>Accredited safeguard Specialist (ASS)</li>
    <li class="wrap">We are not affiliated with any security provider or guard company,<br>&nbsp;&nbsp;we provide independent advise</li>
  </ul>

  <section class="consultant">
    <h2>WHAT TO LOOK FOR IN A SECURITY CONSULTANT</h2>
    <p>A consultant who is Board Certified in Security management</p>
    <p>A consultant who has experience and is considered a expert in corporate security</p>
    <p>A consultant who clearly understands Business and how Security affects the bottom line</p>
    <p>A consultant who is independent who is focused on helping you address your issues.</p>
    <p>A consultant who has worked as a senior manager of a security organization</p>
  </section>

  <section class="services">
    <div class="services-tab">SERVICES OFFERED</div>
    <ul class="col-a">
      <li>Security Management</li>
      <li>Security Management Mentoring/Development</li>
      <li>Risk Assessments</li>
      <li>Security Risk Management</li>
      <li>Security Audits</li>
      <li>Security Performance Testing (Red Team)</li>
      <li>Threat Assessments</li>
      <li>Vulnerability Assessments</li>
    </ul>
    <ul class="col-b">
      <li>Security Planning</li>
      <li>RFP/RFQ</li>
      <li>Project management</li>
      <li>Security Policy Development</li>
      <li>Security Program Review</li>
      <li>Security System Design Management</li>
      <li>High Risk Planning</li>
      <li>Litigation Planning and Consulting</li>
    </ul>
  </section>

  <div class="industries">ENERGY • HEALTHCARE • REAL ESTATE • NUCLEAR • HIGHLY SECURE FACILITIES</div>

  <footer class="contact">
    <span class="phone">
      <svg width="12" height="18" viewBox="0 0 12 18"><rect x="1" y="1" width="10" height="16" rx="2" fill="none" stroke="currentColor" stroke-width="2"/><circle cx="6" cy="14" r="1" fill="currentColor"/></svg>
      Phone: 517-286-4093
    </span>
    <span class="email">
      <svg width="16" height="12" viewBox="0 0 16 12"><rect width="16" height="12" rx="1" fill="currentColor"/><path d="M1 1l7 6 7-6" fill="none" stroke="#fff" stroke-width="1.5"/></svg>
      info@valdrenadvisory.com
    </span>
    <span class="web">
      <svg width="14" height="14" viewBox="0 0 14 14"><circle cx="7" cy="7" r="6" fill="none" stroke="currentColor" stroke-width="1.6"/><path d="M1 7h12M7 1c-3 3-3 9 0 12M7 1c3 3 3 9 0 12" fill="none" stroke="currentColor" stroke-width="1.2"/></svg>
      www.valdrenadvisory.com
    </span>
  </footer>
</div>
</body>
</html>
```